Easter & Summer School Dance Camps

I need two flyers one for Easter camps and one for summer school
We are a performing arts and dance academy

I want a double sided flyers one side summer school one side easter camp

Please make these flyers appeal to young dancers and performers - eye catching up to date Added Tuesday, March 1, 2016

Target Market(s)

Young children and teenagers

Industry/Entity Type

School

Font styles to use
Serif
Sans Serif

Requirements
Must have
• bright colourful

```html
<!DOCTYPE html>
<html lang="en">
<head>
<meta charset="utf-8">
<title>Brightstep Academy – Easter Workshops &amp; Summer School</title>
<link rel="stylesheet" href="https://fonts.googleapis.com/css2?family=Oswald:wght@400;500;600&family=Mulish:wght@400;600;700&family=Abel&family=Roboto+Condensed:wght@300;400&family=Montserrat:wght@800&display=swap">
<style>
  :root {
    --magenta: #c11f68;
    --magenta-deep: #9c1546;
    --swoosh: #f0269a;
    --lime: #e6f02e;
    --divider: #1f5aa8;
    --pink-pale: #f6dcea;
    --pink-light: #fbeef5;
    --navy: #1f3e6c;
    --ink: #1d1d1d;
    --red: #e8202a;
    --burst-fill: #7f8ec9;
    --burst-edge: #2f8f7a;
    --burst-text: #f3f03a;
    --peach: #f9978b;
    --badge-blue: #2c3d9b;
    --white: #ffffff;
  }
  * { margin: 0; padding: 0; box-sizing: border-box; }
  html, body { width: 1200px; height: 843px; overflow: hidden; background: #fff; }
  .flyer { position: relative; width: 1200px; height: 843px; overflow: hidden; }
  address { font-style: normal; }

  /* ---------- Easter side ---------- */
  .easter {
    position: absolute; left: 0; top: 0; width: 596px; height: 843px;
    background: linear-gradient(160deg, var(--magenta) 0%, var(--magenta-deep) 100%);
    color: var(--lime);
    font-family: "Mulish", sans-serif;
  }
  .easter-shapes { position: absolute; inset: 0; }
  .easter-title {
    position: absolute; left: 40px; top: 12px; white-space: nowrap;
    font-family: "Oswald", sans-serif; font-weight: 600;
    font-size: 58px; line-height: 1;
  }
  .intro { position: absolute; left: 21px; font-size: 17.5px; white-space: nowrap; }
  .intro-lead { top: 84px; line-height: 27px; }
  .intro-body { top: 172px; line-height: 24px; }
  .show-name { font-family: "Oswald", sans-serif; font-weight: 500; font-size: 19px; }
  .facts {
    position: absolute; text-align: right; white-space: nowrap;
    font-family: "Oswald", sans-serif; font-weight: 400;
    font-size: 22px; line-height: 30.5px; transform: scaleX(0.85); transform-origin: right top;
  }
  .facts-young { right: 20px; top: 100px; }
  .facts-older { right: 100px; top: 536px; }
  .show-art { position: absolute; display: block; }
  .show-art-once { left: 312px; top: 350px; width: 214px; height: 110px; background: var(--peach); }
  .show-art-west { left: 46px; top: 540px; width: 258px; height: 148px; background: var(--badge-blue); border-radius: 6px; }
  .camps-line {
    position: absolute; left: 0; top: 472px; width: 545px; text-align: center; white-space: nowrap;
    font-size: 19.5px; line-height: 28px;
  }
  .venue { position: absolute; text-align: center; white-space: nowrap; }
  .easter .venue {
    left: 16px; top: 698px; width: 280px; color: var(--white);
    font-family: "Roboto Condensed", sans-serif; font-weight: 300; font-size: 19px; line-height: 25.5px;
  }

  .brand { position: absolute; display: flex; align-items: center; gap: 8px; white-space: nowrap; color: var(--ink); font-family: "Mulish", sans-serif; font-weight: 700; }
  .brand-dot { width: 14px; height: 14px; border-radius: 50%; background: var(--swoosh); flex: none; }
  .brand-name { line-height: 1; }
  .easter .brand { left: 312px; top: 752px; font-size: 25px; }

  .divider { position: absolute; left: 596px; top: 0; width: 8px; height: 843px; background: var(--divider); }

  /* ---------- Summer side ---------- */
  .summer {
    position: absolute; left: 604px; top: 0; width: 596px; height: 843px;
    background: linear-gradient(180deg, var(--pink-light) 0%, var(--pink-pale) 55%, var(--pink-light) 100%);
    color: var(--ink);
  }
  .summer .brand-top { left: 26px; top: 50px; font-size: 26px; }
  .summer-headline {
    position: absolute; left: 228px; top: 32px; white-space: nowrap;
    font-family: "Mulish", sans-serif; font-weight: 400; color: var(--navy);
    font-size: 29px; line-height: 39px;
  }
  .summer-copy {
    position: absolute; left: 17px; width: 553px;
    font-family: "Abel", sans-serif; font-size: 24px; line-height: 31px;
  }
  .summer-copy .line { display: block; text-align: justify; text-align-last: justify; white-space: nowrap; }
  .summer-copy .line-end { display: block; white-space: nowrap; }
  .copy-1 { top: 120px; }
  .copy-2 { top: 240px; }
  .copy-3 { top: 352px; }
  .copy-4 { top: 464px; }
  .disciplines { font-family: "Oswald", sans-serif; font-weight: 500; color: var(--red); font-size: 24px; }
  .burst { position: absolute; left: 68px; top: 530px; width: 464px; height: 198px; }
  .burst-text {
    position: absolute; left: 68px; top: 551px; width: 464px; text-align: center; white-space: nowrap;
    font-family: "Montserrat", sans-serif; font-weight: 800; color: var(--burst-text);
    font-size: 20px; line-height: 26.8px; letter-spacing: 0.5px;
  }
  .summer .venue {
    left: 28px; top: 722px; width: 300px;
    font-family: "Mulish", sans-serif; font-weight: 400; font-size: 16px; line-height: 21.6px; color: var(--ink);
  }
  .summer .venue .email { color: var(--red); }
  .summer .brand-bottom { left: 392px; top: 764px; font-size: 26px; }
</style>
</head>
<body>
<main class="flyer">

  <section class="easter">
    <svg class="easter-shapes" width="596" height="843" viewBox="0 0 596 843" aria-hidden="true">
      <path d="M596 264 C 566 400, 516 520, 504 640 C 496 730, 486 800, 480 843 L 596 843 Z" fill="var(--lime)"/>
      <path d="M0 372 C 60 470, 170 430, 320 300 C 440 190, 520 90, 596 0 C 510 110, 420 220, 300 320 C 170 420, 60 450, 0 372 Z" fill="var(--swoosh)" opacity="0.9"/>
    </svg>

    <h1 class="easter-title">EASTER WORKSHOPS</h1>

    <p class="intro intro-lead">This spring, your child will enjoy a joyous journey<br>to the magical world of <span class="show-name">ONCE UPON A TIME</span> for a<br>fabulous springtime treat.</p>
    <p class="intro intro-body">We will work our magic to ensure your<br>child enjoys every minute. Guiding each<br>child every step of the way and inspire<br>and encourage them to project their<br>voices, learn energetic dance ro-<br>utines, sing catchy songs, and<br>more importantly<br>HAVE FUN!</p>

    <div class="facts facts-young">
      TUESDAY<br>5 &amp; 6<br>APRIL 2016<br>AGE 3 – 7 YEARS<br>10 – 12PM<br>18 PER DAY<br>OR 30 FOR BOTH DAYS
    </div>

    <div class="show-art show-art-once" role="img" aria-label="Once Upon a Time show title lettering"></div>

    <p class="camps-line">Our Easter dance camps are fun, fresh and funky,<br>mixed together with a little musical theatre!</p>

    <div class="show-art show-art-west" role="img" aria-label="West End Workshop title lettering"></div>

    <div class="facts facts-older">
      TUESDAY 5 &amp; 6 APRIL 2016<br>AGE 8 – 16 YEARS<br>1-4 PM<br>30 PER DAY<br>OR 55 FOR BOTH DAYS
    </div>

    <address class="venue">
      Venue<br>The Community Hall of St Anselm<br>Riverford RV4 2AB<br>Email brightstepdance@mailbox<br>to book or text 07700 900123
    </address>

    <div class="brand"><span class="brand-dot"></span><span class="brand-name">Brightstep Academy</span></div>
  </section>

  <div class="divider"></div>

  <section class="summer">
    <div class="brand brand-top"><span class="brand-dot"></span><span class="brand-name">Brightstep</span></div>
    <h2 class="summer-headline">A flash funky flyer that<br>will appeal to teenagers</h2>

    <p class="summer-copy copy-1">
      <span class="line">Summer school is designed for young people who enjoy</span>
      <span class="line">per- forming. The course introduces you to various</span>
      <span class="line-end">disciplines of theatre: <span class="disciplines">ACTING, SINGING AND DANCE.</span></span>
    </p>
    <p class="summer-copy copy-2">
      <span class="line">Everyone is able to develop at their own pace, no-one is</span>
      <span class="line">forced to perform and there are opportunities for you to</span>
      <span class="line-end">explore performance techniques.</span>
    </p>
    <p class="summer-copy copy-3">
      <span class="line">Students will develop key skills in teamwork, communi-</span>
      <span class="line">cation and confidence whilst building friendships and</span>
      <span class="line-end">having fun!</span>
    </p>
    <p class="summer-copy copy-4">
      <span class="line">The week ends with a showing, to friends and family, of</span>
      <span class="line">the skills and musical numbers achieved during the</span>
      <span class="line-end">course.</span>
    </p>

    <svg class="burst" viewBox="0 0 464 188" preserveAspectRatio="none" aria-hidden="true">
      <polygon fill="var(--burst-fill)" stroke="var(--burst-edge)" stroke-width="5" stroke-linejoin="round"
        points="462,94 423,108 444.5,129 394,134 395,159 340,154 320,179 270,165 232,186 194,165 144,179 124,154 69,159 70,134 19.5,129 41,108 2,94 41,80 19.5,59 70,54 69,29 124,34 144,9 194,23 232,2 270,23 320,9 340,34 395,29 394,54 444.5,59 423,80"/>
    </svg>
    <p class="burst-text">BRIGHTSTEP<br>SUMMER SCHOOL<br>A WICKED WEST END WIZ<br>8 AUGUST — 12 AUGUST 2016<br>10 — 4<br>150.00</p>

    <address class="venue">
      Venue<br>The Community Hall of St Anselm<br>Riverford RV4 2AB<br><span class="email">Email brightstepdance@mailbox</span><br>to book or text 07700 900123
    </address>

    <div class="brand brand-bottom"><span class="brand-dot"></span><span class="brand-name">Brightstep</span></div>
  </section>

</main>
</body>
</html>
```